Business Card Design

Consultation for design, construction athletic facilities specializing in synthetic turf systems and all weather running track systems.
Motto "True Owner Representation"
New Company that we'd like to highlight the LOGO first and foremost with the colors of the background and font as primary colors of the card too if possible. I've also attached a typical larger project design layout that could be used in the background to highlight our design and construction specialty.
Website is something we want very noticeable for driving traffic.
Target Market(s)
Athletic Directors, Designers, Government and Military, Contractors
Industry/Entity Type
Construction
Contact Information for Business Card
Peter L. Vandrell CFB, CTB
48317 W 63rd Ave
Harlow Ridge, WA 99482
C +1 503.555.0147
O +1 808.555.0182
Peter@fieldlaneco.example
www.fieldlaneco.example

```html
<!DOCTYPE html>
<html lang="en">
<head>
<meta charset="utf-8">
<title>Kestrel Sport – Business Card</title>
<link rel="stylesheet" href="https://fonts.googleapis.com/css2?family=Crimson+Text:wght@400&family=Open+Sans:wght@400&display=swap">
<style>
  :root {
    --backdrop: #a8a8a8;
    --card-black: #050505;
    --gold: #e9a93c;
    --gold-deep: #f2a516;
    --text-light: #f2f2f2;
    --card-w: 520px;
    --card-h: 300px;
    --radius: 16px;
  }
  * { box-sizing: border-box; margin: 0; padding: 0; }
  html, body {
    width: 1200px;
    height: 900px;
    overflow: hidden;
    background: var(--backdrop);
  }
  .stage {
    width: 1200px;
    height: 900px;
    display: flex;
    align-items: center;
    justify-content: center;
    gap: 60px;
  }
  .card {
    position: relative;
    width: var(--card-w);
    height: var(--card-h);
    border-radius: var(--radius);
    background: var(--card-black);
    overflow: hidden;
    box-shadow: 0 18px 30px rgba(0,0,0,0.35);
  }

  /* Company name placeholder: one font, one weight, one colour */
  .company-name {
    position: absolute;
    font-family: "Open Sans", Arial, sans-serif;
    font-weight: 400;
    color: var(--gold);
    line-height: 1;
    white-space: nowrap;
  }

  /* Front */
  .card-front .company-name { left: 120px; top: 112px; font-size: 40px; }
  .web-band {
    position: absolute;
    left: 0; right: 0;
    bottom: 26px;
    height: 44px;
    background: linear-gradient(90deg, var(--card-black) 20%, #3a2608 45%, var(--gold-deep) 100%);
    display: flex;
    align-items: center;
    justify-content: flex-end;
    padding-right: 22px;
    font-family: "Open Sans", Arial, sans-serif;
    font-size: 21px;
    letter-spacing: 0.04em;
    color: var(--text-light);
  }

  /* Back */
  .card-back .company-name { left: 112px; top: 66px; font-size: 30px; }
  .light-burst {
    position: absolute;
    right: -90px;
    top: -70px;
    width: 300px;
    height: 260px;
    background: radial-gradient(circle at 70% 30%, rgba(255,236,180,0.95) 0%, rgba(255,180,58,0.7) 14%, rgba(230,130,20,0.3) 38%, rgba(0,0,0,0) 68%);
  }
  .glitter-field {
    position: absolute;
    left: 0; right: 0; bottom: 0;
    height: 150px;
    background: radial-gradient(ellipse at 40% 100%, rgba(200,140,40,0.28) 0%, rgba(120,80,20,0.12) 45%, rgba(0,0,0,0) 75%);
  }
  .contact {
    position: absolute;
    left: 40px;
    top: 160px;
    font-family: "Open Sans", Arial, sans-serif;
    color: var(--text-light);
  }
  .contact-name {
    font-family: "Crimson Text", Georgia, serif;
    font-size: 23px;
    color: var(--gold);
    line-height: 1.1;
  }
  .contact-name .credential { font-family: "Open Sans", Arial, sans-serif; font-size: 13px; color: var(--text-light); margin-left: 8px; }
  .contact-address { font-size: 13px; margin-top: 3px; }
  .contact-list { list-style: none; margin-top: 7px; }
  .contact-list li {
    display: flex;
    align-items: center;
    gap: 14px;
    font-size: 14.5px;
    line-height: 19px;
  }
  .contact-list svg { width: 11px; height: 11px; flex: none; }
</style>
</head>
<body>
<main class="stage">

  <section class="card card-front" aria-label="Business card front">
    <p class="company-name">Kestrel Sport</p>
    <div class="web-band">www.fieldlaneco.example</div>
  </section>

  <section class="card card-back" aria-label="Business card back">
    <div class="light-burst" role="img" aria-label="Radiating golden light rays in the top right corner"></div>
    <div class="glitter-field" role="img" aria-label="Scattered gold glitter particles across the lower card"></div>
    <p class="company-name">Kestrel Sport</p>
    <div class="contact">
      <p class="contact-name">Peter L. Vandrell<span class="credential">CFB</span></p>
      <p class="contact-address">CTB 48317 W 63rd Ave Harlow Ridge, WA 99482 C</p>
      <ul class="contact-list">
        <li>
          <svg viewBox="0 0 12 12" aria-hidden="true"><rect x="3" y="0.5" width="6" height="11" rx="1" fill="none" stroke="#e9a93c" stroke-width="1.2"/></svg>
          +1 503.555.0147
        </li>
        <li>
          <svg viewBox="0 0 12 12" aria-hidden="true"><path d="M1 4 Q6 0 11 4 L10 6 L8 5 L8 4 Q6 3 4 4 L4 5 L2 6 Z" fill="#e9a93c"/><rect x="2.5" y="7" width="7" height="4" rx="0.8" fill="#e9a93c"/></svg>
          +1 808.555.0182
        </li>
        <li>
          <svg viewBox="0 0 12 12" aria-hidden="true"><rect x="0.5" y="2.5" width="11" height="7" fill="#e9a93c"/><path d="M0.5 2.5 L6 7 L11.5 2.5" fill="none" stroke="#050505" stroke-width="1"/></svg>
          Peter@fieldlaneco.example
        </li>
        <li>
          <svg viewBox="0 0 12 12" aria-hidden="true"><circle cx="6" cy="6" r="5.2" fill="none" stroke="#e9a93c" stroke-width="1"/><ellipse cx="6" cy="6" rx="2.2" ry="5.2" fill="none" stroke="#e9a93c" stroke-width="0.9"/><line x1="0.8" y1="6" x2="11.2" y2="6" stroke="#e9a93c" stroke-width="0.9"/></svg>
          www.fieldlaneco.example
        </li>
      </ul>
    </div>
  </section>

</main>
</body>
</html>
```